The Maplewick Greenhouse Garden Nursery Cards

We are looking for a professional nice business card for the Garden Center. I attached our current cards so you have the information. We do have 2 locations so that is also listed. We like the brown fade in the front, but if you have other ideas that is fine.

Also the back of the card we would like to have the ariel picture of the nursery on the card. I have that picture attached.

I also uploaded our logo files for you.

Target Market(s)

Retail

Industry/Entity Type

Retail Garden Center

Contact Information for Business Card

I have uploaded card samples.

Colors

Designer to choose colors to be used in the design.

Requirements
Must have
• Name, email, phone, cell, locations

```html
<!DOCTYPE html>
<html lang="en">
<head>
<meta charset="utf-8">
<title>The Maplewick Greenhouse – Business Cards</title>
<link href="https://fonts.googleapis.com/css2?family=Montserrat:wght@400;500;700;800&display=swap" rel="stylesheet">
<style>
  :root {
    --backdrop: #d9d6d1;
    --brown-dark: #4a2a1f;
    --brown-mid: #5a3526;
    --brown-light: #7a5444;
    --photo-dark: #5b3d2c;
    --photo-light: #8a6a50;
    --gold: #f2a516;
    --cream: #fbf2b0;
    --cream-text: #fdf4d8;
    --white: #ffffff;
    --line: #c9a34a;
  }
  * { box-sizing: border-box; margin: 0; padding: 0; }
  html, body { width: 1200px; height: 822px; overflow: hidden; }
  body {
    background: var(--backdrop);
    font-family: "Montserrat", sans-serif;
    position: relative;
  }
  .card {
    position: absolute;
    width: 640px;
    height: 366px;
    border-radius: 22px;
    overflow: hidden;
    box-shadow: 0 10px 28px rgba(0,0,0,.25);
  }
  /* Back of card */
  .card--back { left: 60px; top: 60px; }
  .aerial-photo {
    position: absolute; inset: 0;
    background: linear-gradient(150deg, var(--photo-light) 0%, var(--photo-dark) 55%, var(--brown-mid) 100%);
  }
  .brand {
    position: absolute;
    display: flex; align-items: center; gap: 12px;
    color: var(--cream-text);
    font-weight: 700;
  }
  .brand__dot { border-radius: 50%; background: var(--gold); flex: none; }
  .card--back .brand { left: 50%; top: 50%; transform: translate(-50%, -50%); font-size: 28px; white-space: nowrap; }
  .card--back .brand__dot { width: 30px; height: 30px; }

  /* Front of card */
  .card--front {
    left: 500px; top: 402px;
    background: linear-gradient(100deg, var(--brown-dark) 0%, var(--brown-mid) 55%, var(--brown-light) 100%);
  }
  .card--front .brand {
    left: 40px; top: 118px; width: 260px;
    flex-direction: column; text-align: center; gap: 10px;
    font-size: 26px; line-height: 1.15;
  }
  .card--front .brand__dot { width: 34px; height: 34px; }
  .divider {
    position: absolute; left: 318px; top: 72px;
    width: 1px; height: 196px; background: var(--line);
  }
  .contact { position: absolute; left: 338px; top: 34px; color: var(--white); }
  .contact__name { color: var(--gold); font-weight: 800; font-size: 26px; letter-spacing: .3px; }
  .contact__role { font-size: 13px; margin-bottom: 8px; }
  .location { font-size: 12.5px; line-height: 1.3; margin-bottom: 6px; }
  .location__city { font-weight: 700; }
  .contact__list { list-style: none; font-size: 12.5px; line-height: 1.5; }
  .contact__list li { display: flex; align-items: center; gap: 8px; }
  .icon { width: 12px; height: 12px; flex: none; }
  .bands { position: absolute; left: 0; bottom: 0; width: 640px; height: 80px; }
  .band-text {
    position: absolute; display: flex; align-items: center; gap: 8px;
    font-size: 13px; font-weight: 500;
  }
  .band-text--email { left: 30px; bottom: 14px; color: var(--brown-dark); }
  .band-text--web { right: 28px; bottom: 50px; color: var(--white); }
</style>
</head>
<body>

<section class="card card--back">
  <div class="aerial-photo" role="img" aria-label="Aerial photograph of the nursery grounds, greenhouses and parking lot under a brown tint"></div>
  <div class="brand"><span class="brand__dot"></span>The Maplewick Greenhouse</div>
</section>

<section class="card card--front">
  <div class="brand"><span class="brand__dot"></span>The Maplewick Greenhouse</div>
  <div class="divider"></div>

  <div class="contact">
    <p class="contact__name">RHETT CALLOWAY</p>
    <p class="contact__role">Director</p>
    <div class="location">
      <p class="location__city">Brookhaven</p>
      <p>4120 Orchard Lane Rd</p>
      <p>Brookhaven, FL 33610</p>
    </div>
    <div class="location">
      <p class="location__city">Cedar Bluff</p>
      <p>27640 County Road 19</p>
      <p>Cedar Bluff, FL 33598</p>
    </div>
    <ul class="contact__list">
      <li><svg class="icon" viewBox="0 0 12 12"><path d="M2 1l2 0 1 3-1.5 1a6 6 0 0 0 3.5 3.5L8 7l3 1v2a1 1 0 0 1-1 1A9 9 0 0 1 1 2a1 1 0 0 1 1-1z" fill="var(--gold)"/></svg>352-555-0142</li>
      <li><svg class="icon" viewBox="0 0 12 12"><rect x="3" y="0.5" width="6" height="11" rx="1" fill="none" stroke="var(--gold)" stroke-width="1.3"/><circle cx="6" cy="9.6" r=".8" fill="var(--gold)"/></svg>352-555-0187</li>
      <li><svg class="icon" viewBox="0 0 12 12"><rect x="0.5" y="2" width="11" height="8" fill="var(--gold)"/><path d="M0.5 2L6 7l5.5-5" fill="none" stroke="var(--brown-dark)" stroke-width="1"/></svg>rhett@maplewickgreenhouse.com</li>
    </ul>
  </div>

  <svg class="bands" viewBox="0 0 640 80" preserveAspectRatio="none" aria-hidden="true">
    <polygon points="0,44 400,44 384,80 0,80" fill="var(--cream)"/>
    <polygon points="412,44 424,10 640,10 640,44 430,44 416,70" fill="var(--gold)"/>
  </svg>
  <div class="band-text band-text--email">
    <svg class="icon" viewBox="0 0 12 12"><rect x="0.5" y="2" width="11" height="8" fill="none" stroke="var(--brown-dark)" stroke-width="1.2"/><path d="M0.5 2L6 7l5.5-5" fill="none" stroke="var(--brown-dark)" stroke-width="1.2"/></svg>
    sales@maplewickgreenhouse.com
  </div>
  <div class="band-text band-text--web">
    <svg class="icon" viewBox="0 0 12 12" fill="none" stroke="var(--white)" stroke-width="1"><circle cx="6" cy="6" r="5.3"/><ellipse cx="6" cy="6" rx="2.3" ry="5.3"/><path d="M0.7 6h10.6M1.5 3.3h9M1.5 8.7h9"/></svg>
    www.maplewickgreenhouse.com
  </div>
</section>

</body>
</html>
```